Patent Law

Need to develop a home page for a patent lawyer.

Colors should go with logo, blues...

Company Name- Corvel Tindry, PLLC

Company Overview-

I am an Intellectual Property Lawyer and focus on patents, copyrights, trademarks, & trade secrets. I work with small businesses and start ups in the chemical and biotech industries.

Why Us-

I am small firm that can provide large-firm service at a reasonable price. I also can charge flat-fees for entreprenuers in certain practice areas.

Services-
Intellectual Property
Patents
Copyrights
Trademarks
Trade secrets
Healthcare Compliance
Elder law
Wills
Trusts

Website we like-
http://www.quarnlowtide.example/ - within industry!!
http://www.vopperhask.example/
http://dulbrickovan.example/
http://thefernwoldguides.example/

Target Market(s)

My customers will be small business, specifically small start-up companies in the chemical and biotech arena.

Industry/Entity Type

Trade

Requirements
Must have
• Colors should go with logo, blues...

```html
<!DOCTYPE html>
<html lang="en">
<head>
<meta charset="utf-8">
<title>Corvel Tindry, PLLC</title>
<link rel="stylesheet" href="https://fonts.googleapis.com/css2?family=Open+Sans:wght@300;400;600&display=swap">
<style>
:root{
  --blue:#1f8fd0;
  --blue-dark:#0f5f95;
  --ink:#222;
  --grey:#666;
  --row:#ececec;
  --icon:#7a7a7a;
  --footer:#1f1f1f;
  --footer-text:#9a9a9a;
  --sky-a:#3e86c9;
  --sky-b:#a9dbef;
}
*{box-sizing:border-box;margin:0;padding:0}
html,body{width:1006px;height:1200px;overflow:hidden;background:#fff}
body{position:relative;font-family:"Open Sans",Arial,sans-serif;color:var(--ink)}
.abs{position:absolute}
/* header */
.brand{left:110px;top:40px;display:flex;align-items:center;gap:8px}
.brand-dot{width:22px;height:22px;border-radius:50%;background:var(--blue-dark)}
.brand-name{font-size:15px;font-weight:400;color:var(--blue-dark);letter-spacing:.5px}
.enquiry{left:710px;top:14px;display:flex;gap:10px;align-items:flex-start}
.enquiry small{display:block;font-size:11.5px;color:#444;line-height:13px}
.enquiry strong{display:block;font-size:16px;font-weight:400;color:var(--blue);line-height:18px}
.globe{left:868px;top:15px}
.nav{left:365px;top:89px;display:flex;gap:0;list-style:none;font-size:11.5px;color:#666}
.nav li{margin-right:20px}
.nav li.active{color:var(--blue)}
.search{left:715px;top:84px;width:182px;height:24px;border-radius:12px;background:#eee;display:flex;align-items:center;padding-left:8px;gap:10px;font-size:11px;color:#aaa}
/* hero */
.hero{left:0;top:116px;width:1006px;height:472px;background:radial-gradient(ellipse at 60% 20%,var(--sky-b),var(--sky-a) 75%)}
.hero-figure{left:690px;top:130px;width:270px;height:342px;background:linear-gradient(160deg,#c99a6d,#8e6343);border-radius:120px 120px 0 0}
.hero-title{left:108px;top:110px;font-size:84px;font-weight:600;color:#fff;line-height:1}
.hero-sub{left:107px;top:200px;font-size:37px;font-weight:400;color:#fff}
.hero-text{left:109px;top:250px;width:480px;font-size:19px;line-height:19px;color:#fff}
.hero-btn{left:410px;top:302px;width:156px;height:40px;border-radius:4px;background:linear-gradient(#1684c0,#0a5f8f);border:2px solid #36b1e6;color:#fff;font-size:14.5px;display:flex;align-items:center;justify-content:center}
.dots{left:453px;top:430px;display:flex;gap:18px}
.dots span{width:11px;height:11px;border-radius:50%;background:#fff}
.dots span.on{border:3px solid var(--blue-dark)}
/* columns */
.col-head{top:645px;font-size:16px;font-weight:400;color:#111;letter-spacing:.3px}
.photo{top:676px}
.why-title{left:111px;top:871px;font-size:14px;color:#333}
.why-text{left:111px;top:891px;width:237px;font-size:11px;line-height:17px;color:#555;text-align:justify;font-weight:300}
.more{top:973px;font-size:13px;font-style:italic;color:var(--blue);font-weight:300}
.services{left:390px;top:676px;width:227px;list-style:none}
.services li{height:34px;margin-bottom:3px;background:var(--row);display:flex;align-items:center;font-size:13px;color:var(--blue)}
.services svg{width:34px;margin-right:19px;flex:none}
.contact-line{left:664px;display:flex;gap:14px;align-items:flex-start}
.contact-line small{display:block;font-size:11.5px;color:#444;line-height:12px}
.contact-line strong{display:block;font-weight:400;color:var(--blue);line-height:17px}
/* footer */
.footer{left:0;top:1064px;width:1006px;height:136px;background:var(--footer);border-top:5px solid var(--blue)}
.footer-name{left:109px;top:1103px;font-size:12.5px;font-weight:600;color:var(--footer-text)}
.footer-info{left:109px;top:1127px;font-size:11.5px;line-height:16px;color:#bbb}
.footer-info span{font-size:9px;color:var(--footer-text)}
.footer-divider{left:384px;top:1083px;width:1px;height:90px;background:#444}
.social{left:803px;top:1087px;display:flex;gap:6px}
.social span{width:27px;height:27px;border-radius:50%;background:#8a8a8a}
.copyright{right:110px;top:1162px;font-size:11px;color:#6d6d6d;font-weight:300}
</style>
</head>
<body>
<header>
  <div class="abs brand"><span class="brand-dot"></span><span class="brand-name">CORVEL TINDRY, PLLC</span></div>
  <div class="abs enquiry">
    <svg width="16" height="25" viewBox="0 0 16 25"><rect x="1" y="1" width="14" height="23" rx="2" fill="#111"/><rect x="3" y="4" width="10" height="15" fill="#fff"/><circle cx="8" cy="21.5" r="1.2" fill="#fff"/></svg>
    <div><small>call us for enquiries</small><strong>005550100200</strong></div>
  </div>
  <svg class="abs globe" width="27" height="27" viewBox="0 0 27 27"><circle cx="13.5" cy="13.5" r="12" fill="#fff" stroke="#111" stroke-width="2"/><path d="M7 8c3-1 5 1 6 3s-2 3-1 6-3 3-4 1-3-4-1-6zM15 6c2 0 5 2 6 5s-1 5-3 6-2-3-3-4 0-5 0-7z" fill="#111"/></svg>
  <ul class="abs nav"><li class="active">HOME</li><li>FIRM</li><li>PEOPLE</li><li>PRACTICES</li><li>LIBRARY</li><li>NEWS</li></ul>
  <div class="abs search"><svg width="15" height="15" viewBox="0 0 15 15"><circle cx="6" cy="6" r="4.5" fill="none" stroke="#2a8fd0" stroke-width="2.2"/><path d="M9.3 9.3l4 4" stroke="#2a8fd0" stroke-width="2.5" stroke-linecap="round"/></svg>search</div>
</header>

<section class="abs hero">
  <div class="abs hero-figure" role="img" aria-label="Statue of blindfolded Lady Justice holding scales against the sky"></div>
  <h1 class="abs hero-title">WHAT</h1>
  <h2 class="abs hero-sub">Makes us different ?</h2>
  <p class="abs hero-text">We have a one-on-one, very personal approach that isn't typical of many client-attorney relationships.</p>
  <div class="abs hero-btn">Know more</div>
  <div class="abs dots"><span class="on"></span><span></span><span></span><span></span></div>
</section>

<main>
  <h3 class="abs col-head" style="left:109px">WELCOME</h3>
  <div class="abs photo" style="left:111px;width:237px;height:175px;background:linear-gradient(135deg,#5a3a22,#2a1a10 60%,#7a5030)" role="img" aria-label="Brass scales of justice and a gavel on a desk"></div>
  <h4 class="abs why-title">Why us ?</h4>
  <p class="abs why-text">On it, we intend to inform you about what we do and about issues that may be important to you. Our most important service is personal attention to individual issues.</p>
  <span class="abs more" style="left:295px">more...</span>

  <h3 class="abs col-head" style="left:390px">WHAT WE DO</h3>
  <ul class="abs services">
    <li><svg height="20" viewBox="0 0 34 20"><rect x="15" y="9" width="9" height="10" rx="2" fill="#7a7a7a"/><path d="M17 9V5a3 3 0 0 1 6 0" fill="none" stroke="#7a7a7a" stroke-width="2"/></svg>Intellectual Property</li>
    <li><svg height="20" viewBox="0 0 34 20"><rect x="14" y="1" width="13" height="17" fill="none" stroke="#7a7a7a" stroke-width="1.8"/><path d="M17 6h7M17 9h7M17 12h4" stroke="#7a7a7a" stroke-width="1.5"/><circle cx="26" cy="16" r="3" fill="#7a7a7a"/></svg>Patents</li>
    <li><svg height="20" viewBox="0 0 34 20"><circle cx="20" cy="10" r="8" fill="none" stroke="#7a7a7a" stroke-width="2"/><path d="M23 7a4 4 0 1 0 0 6" fill="none" stroke="#7a7a7a" stroke-width="2"/></svg>Copyrights</li>
    <li><svg height="20" viewBox="0 0 34 20"><circle cx="20" cy="10" r="8" fill="none" stroke="#7a7a7a" stroke-width="2"/><path d="M17 15V5h4a2.5 2.5 0 0 1 0 5h-4M20 10l3 5" fill="none" stroke="#7a7a7a" stroke-width="2"/></svg>Trademarks</li>
    <li><svg height="20" viewBox="0 0 34 20"><circle cx="17" cy="10" r="4" fill="#7a7a7a"/><path d="M20 10h13M27 10v3M30 10v3" stroke="#7a7a7a" stroke-width="2"/></svg>Trade secrets</li>
    <li><svg height="22" viewBox="0 0 34 22"><path d="M15 2v7a5 5 0 0 0 10 0V2M20 14v3a4 4 0 0 0 8 0v-4" fill="none" stroke="#7a7a7a" stroke-width="1.8"/><circle cx="28" cy="11" r="2" fill="#7a7a7a"/></svg>Healthcare Compliance</li>
    <li><svg height="22" viewBox="0 0 34 22"><circle cx="19" cy="3" r="2" fill="#7a7a7a"/><path d="M19 6v7h6l2 6" fill="none" stroke="#7a7a7a" stroke-width="2"/><path d="M16 11a6 6 0 1 0 8 7" fill="none" stroke="#7a7a7a" stroke-width="2"/></svg>Elder law</li>
    <li><svg height="22" viewBox="0 0 34 22"><rect x="14" y="2" width="13" height="18" fill="none" stroke="#7a7a7a" stroke-width="1.8"/><path d="M17 7h7M17 10h7M17 13h5" stroke="#7a7a7a" stroke-width="1.5"/><path d="M22 19l6-8" stroke="#7a7a7a" stroke-width="2"/></svg>Wills</li>
  </ul>
  <span class="abs more" style="left:575px">more...</span>

  <h3 class="abs col-head" style="left:658px">CONTACT US</h3>
  <div class="abs photo" style="left:659px;width:238px;height:173px;background:linear-gradient(120deg,#f2f4f6,#d8e4ee 55%,#9fbfdc)" role="img" aria-label="Customer support staff wearing headsets"></div>
  <div class="abs contact-line" style="top:876px">
    <svg width="16" height="25" viewBox="0 0 16 25"><rect x="1" y="1" width="14" height="23" rx="2" fill="#111"/><rect x="3" y="4" width="10" height="15" fill="#fff"/><circle cx="8" cy="21.5" r="1.2" fill="#fff"/></svg>
    <div><small>call us for enquiries</small><strong style="font-size:16px">005550100200</strong></div>
  </div>
  <div class="abs contact-line" style="top:919px">
    <svg width="22" height="14" viewBox="0 0 22 14" style="margin-top:6px"><rect width="22" height="14" fill="#111"/><path d="M1 1l10 7 10-7M1 13l8-6M21 13l-8-6" fill="none" stroke="#fff" stroke-width="1.2"/></svg>
    <div><small>email to us</small><strong style="font-size:12px">contact@corveltindry.example</strong></div>
  </div>
  <span class="abs more" style="left:856px">more...</span>
</main>

<footer>
  <div class="abs footer"></div>
  <div class="abs footer-name">CORVEL TINDRY PLLC</div>
  <div class="abs footer-info"><span>E-MAIL:</span> info@tindrylawoffice.example<br><span>PHONE:</span> <b style="font-weight:400;font-size:14px">555 010 4477</b></div>
  <div class="abs footer-divider"></div>
  <div class="abs social"><span></span><span></span><span></span></div>
  <div class="abs copyright">© Copyright 2014 . All rights reserved to CORVEL TINDRY PLLC</div>
</footer>
</body>
</html>
```